Vision Board Class Design needed

Hello, I need a business card design for a new Company based in Mount Waverley, Victoria, Australia. The Company provides a training Class with approx. 5 guests. They learn how to choose and create positive things in their life. It is based on the principal of the Law of Attraction. Each guest receives a large coloured cardboard and magazines, affirmations to choose ideas to help create their new exciting life - all pasted onto a "Vision Board" which will be seen by them every day and help to clarify the vision and attract abundance, happiness & positivity into their lives. I would like to see designs with bright, happy colours - perhaps rainbows - anything that represents a new life and appears refreshing.
Many thanks.

Industry/Entity Type

Training

Contact Information for Business Card

Bright Horizon
Delia
Mobile 0473 206-558

Logo Text

Bright Horizon

Logo styles of interest
Abstract Logo
Requirements
Must have
• Happy, Bright colours!

```html
<!DOCTYPE html>
<html lang="en">
<head>
<meta charset="utf-8">
<title>Bright Horizon – Business Card</title>
<link rel="stylesheet" href="https://fonts.googleapis.com/css2?family=Questrial&display=swap">
<style>
  :root {
    --page-bg: #ecebe8;
    --card-bg: #ffffff;
    --ink: #1e1e1e;
    --brand: #9a68b3;
    --purple: #a66db4;
    --yellow: #f5e21a;
    --blue: #4b9ad6;
    --orange: #f6921e;
    --green: #6bbb45;
    --bubble-edge: #c9e3e6;
    --bubble-core: #ffffff;
    --card-shadow: 0 10px 28px rgba(0, 0, 0, 0.22);
  }

  * { box-sizing: border-box; margin: 0; padding: 0; }

  html, body {
    width: 960px;
    height: 1200px;
    overflow: hidden;
    background: var(--page-bg);
    font-family: "Questrial", "Century Gothic", sans-serif;
  }

  .sheet {
    position: relative;
    width: 960px;
    height: 1200px;
  }

  .card {
    position: absolute;
    left: 80px;
    width: 800px;
    height: 470px;
    background: var(--card-bg);
    box-shadow: var(--card-shadow);
    overflow: hidden;
  }

  .card--front { top: 90px; }
  .card--back  { top: 640px; }

  .brand-name {
    font-family: "Questrial", "Century Gothic", sans-serif;
    color: var(--brand);
    font-weight: 400;
    letter-spacing: 0.06em;
    text-transform: uppercase;
    white-space: nowrap;
  }

  /* Front */
  .front-details {
    position: absolute;
    left: 120px;
    top: 150px;
    width: 460px;
    text-align: center;
  }

  .front-details .brand-name {
    font-size: 46px;
  }

  .contact-name {
    margin-top: 40px;
    font-size: 30px;
    color: var(--ink);
  }

  .contact-phone {
    margin-top: 6px;
    font-size: 20px;
    letter-spacing: 0.04em;
    color: var(--ink);
  }

  .front-figure {
    position: absolute;
    right: 36px;
    bottom: 0;
    width: 150px;
    height: 250px;
    background: var(--blue);
    border-radius: 75px 75px 0 0;
  }

  /* Back */
  .speech-band {
    position: absolute;
    left: 48px;
    top: 34px;
    width: 704px;
    height: 120px;
    border-radius: 40px;
    background: radial-gradient(ellipse at center, var(--bubble-core) 55%, var(--bubble-edge) 100%);
    display: flex;
    align-items: center;
    justify-content: center;
  }

  .speech-band .brand-name {
    font-size: 58px;
  }

  .crowd {
    position: absolute;
    left: 28px;
    right: 28px;
    top: 180px;
    bottom: 0;
    border-radius: 60px 60px 0 0;
    background: linear-gradient(90deg,
      var(--purple) 0%, var(--purple) 16%,
      var(--yellow) 24%, var(--yellow) 36%,
      var(--blue) 44%, var(--blue) 56%,
      var(--orange) 64%, var(--orange) 76%,
      var(--green) 84%, var(--green) 100%);
  }
</style>
</head>
<body>
  <main class="sheet">
    <section class="card card--front" aria-label="Business card front">
      <div class="front-details">
        <p class="brand-name">Bright Horizon</p>
        <p class="contact-name">Delia</p>
        <p class="contact-phone">0473 206-558</p>
      </div>
      <div class="front-figure" role="img" aria-label="Illustration of a blue standing person with a white heart on the chest"></div>
    </section>

    <section class="card card--back" aria-label="Business card back">
      <div class="speech-band">
        <p class="brand-name">Bright Horizon</p>
      </div>
      <div class="crowd" role="img" aria-label="Illustration of five standing people in purple, yellow, blue, orange and green, each with a white heart, speaking together"></div>
    </section>
  </main>
</body>
</html>
```